HR Outsourcing and Payroll Company needs a website re-design

The client is LarkfieldHR: www .larkfield-hr. example

They provide services to other businesses, specifically Human Resources (HR) Outsourcing and Payroll services. They are not happy with their current website and have retained our agency to provide a re-design.

You will design 4 pages for us to show the client. They will select a design they like. My agency will take the winning design and files and design the remaining pages of the site. But, we need you to help us establish a design for the basics so they can select a direction.

We need a Homepage design, a Service Page design, a Broker page design, and a Contact page design.

They really like these websites (in order from most preferred look and feel of imagery and design elements), so I think a mix between the two would be great:

https://www.brisvane.example/
http://www.quelmora.example/

I have attached a project brief for this website. Please refer to it... It will help you be successful in what you deliver. The best designs will incorporate functionality and elements from the project brief.

Target Market(s)

Business owners. They will be thinking about thinks like employee reviews, payroll, time keeping, hiring, being compliant with state laws, and needing an expert to help them.

Industry/Entity Type

It Company

Number of Pages Required

4 page

Font styles to use
Sans Serif

Colors
f37122
0255a3
fbed22
9bcb3c
ec1f27

Requirements
Must have
• We need:
• -Homepage design (desktop and mobile)
• -Service Page design (desktop and mobile)
• -Broker page design (desktop and mobile)
• -Contact page design (desktop and mobile)
• Inspiration: a mix between the two would be great:
• https://www.brisvane.example/
• http://www.quelmora.example/
• They like the long extended homepage look:
• http://www.quelmora.example/
• Photos that have focused people in the front and blurred backgrounds. Example: https://www.brisvane.example/
• Graphic Icons for their services. Example:
• http://www.quelmora.example/
• I have attached a project brief for this website. Please refer to it... It will help you be successful in what you deliver. The best designs will incorporate functionality and elements from the project brief.
Should not have
• Crappy stock photos... you can use watermarked stock photos if you don't wish to purchase them for the sake of the contest.

```html
<!DOCTYPE html>
<html lang="en">
<head>
<meta charset="utf-8">
<title>LarkfieldHR — Human Resources</title>
<link href="https://fonts.googleapis.com/css2?family=Raleway:wght@300;400;500;600;700;800&family=Open+Sans:wght@400;600;700&display=swap" rel="stylesheet">
<style>
:root{
  --blue:#0255a3;
  --blue-deep:#0a3f7e;
  --orange:#f37122;
  --ink:#222;
  --text:#555;
  --muted:#8a8a8a;
  --light:#f4f4f4;
  --dark:#2d3139;
  --darker:#1f2228;
  --field:#6b6e73;
  --white:#fff;
}
*{box-sizing:border-box;margin:0;padding:0}
html,body{width:1200px;height:3243px;overflow:hidden}
body{position:relative;background:var(--white);font-family:"Open Sans",Arial,sans-serif;color:var(--text)}
.abs{position:absolute}
a{color:inherit;text-decoration:none}

/* header */
.topbar{left:0;top:0;width:1200px;height:32px;background:var(--blue);color:#fff;font:600 13px "Open Sans",sans-serif}
.topbar .phone{left:184px;top:7px;display:flex;align-items:center;gap:8px}
.topbar .account{left:860px;top:8px;display:flex;gap:0;align-items:center}
.topbar .account span{padding:0 14px;border-right:1px solid rgba(255,255,255,.6);line-height:17px;font-size:12px}
.topbar .account span:first-child{padding-left:0}
.topbar .search{left:1040px;top:6px}
.mainnav{left:0;top:32px;width:1200px;height:65px;background:#f7f7f7;border-bottom:1px solid #e5e5e5}
.mainnav a{position:absolute;top:25px;font:700 15px "Raleway",sans-serif;color:var(--blue);letter-spacing:.5px}
.brand-disc{left:480px;top:-130px;width:240px;height:270px;border-radius:0 0 120px 120px;background:#fff;z-index:5;display:flex;align-items:flex-end;justify-content:center;padding-bottom:64px}
.brand-name{font:700 30px "Raleway",sans-serif;color:var(--blue);letter-spacing:.5px}

/* hero */
.hero{left:0;top:97px;width:1200px;height:487px;background:radial-gradient(ellipse at 50% 40%,#3b8fe0 0%,#1565c0 45%,#0b3f86 100%)}
.hero h1{position:absolute;left:0;width:1200px;top:80px;text-align:center;font:300 47px "Raleway",sans-serif;color:#fff;letter-spacing:1px}
.hero .cta{left:458px;top:387px;width:288px;height:67px;background:#0a4e92;color:#fff;display:flex;align-items:center;justify-content:center;font:600 17px "Raleway",sans-serif;letter-spacing:.5px}
.slider-arrow{top:205px;width:39px;height:104px;background:rgba(230,230,230,.9);display:flex;align-items:center;justify-content:center}

/* services */
.services{left:0;top:584px;width:1200px;height:616px;background:var(--light)}
.intro{left:0;top:42px;width:1200px;text-align:center;font:500 24px/36px "Raleway",sans-serif;color:var(--blue)}
.card{top:155px;width:188px;height:392px;background:#fff;border-top:3px solid var(--orange);box-shadow:0 1px 4px rgba(0,0,0,.08);text-align:center}
.card svg{margin-top:24px}
.card h3{margin-top:10px;font:600 15px/20px "Open Sans",sans-serif;color:#333;min-height:40px}
.card ul{list-style:none;text-align:left;padding:2px 16px 0 34px}
.card li{position:relative;font:12px/15px "Open Sans",sans-serif;color:#888;margin-bottom:11px}
.card li::before{content:"";position:absolute;left:-12px;top:6px;width:4px;height:4px;border-radius:50%;background:#bbb}
.btn{background:var(--orange);color:#fff;font:700 14px "Raleway",sans-serif;letter-spacing:.5px;display:flex;align-items:center;justify-content:center;box-shadow:0 3px 4px rgba(0,0,0,.18)}
.card .btn{position:absolute;left:22px;bottom:30px;width:143px;height:39px}

/* stats */
.stats{left:0;top:1200px;width:1200px;height:357px;background:linear-gradient(180deg,#3a3f48 0%,#2a2e36 100%)}
.stats h2{position:absolute;left:0;top:44px;width:1200px;text-align:center;font:500 26px "Open Sans",sans-serif;color:#fff}
.stat{top:128px;width:190px;text-align:center;color:#fff}
.stat .num{margin-top:14px;font:600 21px "Open Sans",sans-serif}
.stat .label{margin-top:10px;font:700 11px/19px "Open Sans",sans-serif;color:#e6e6e6}

/* blog */
.blog{left:0;top:1557px;width:1200px;height:594px;background:#fff}
.blog h2{position:absolute;top:36px;left:0;width:1200px;text-align:center;font:600 32px "Raleway",sans-serif;color:var(--blue)}
.post{top:113px;width:320px}
.post h3{font:600 19px "Open Sans",sans-serif;color:#222;letter-spacing:1.2px}
.post p{margin-top:8px;font:17px/23px "Open Sans",sans-serif;color:#666}
.post .photo{margin-top:20px;width:320px;height:212px;background:linear-gradient(135deg,#cfd4db 0%,#8f98a6 45%,#4b5361 100%)}
.post .more{display:block;margin-top:20px;font:800 18px "Raleway",sans-serif;color:var(--orange);letter-spacing:1px}
.blog .btn{left:515px;top:508px;width:160px;height:47px;font-size:18px}

/* testimonial */
.testimonial{left:0;top:2151px;width:1200px;height:379px;overflow:hidden}
.testimonial .backdrop{position:absolute;inset:0;background:linear-gradient(90deg,#5f646c 0%,#7b8088 60%,#8a8f96 100%)}
.testimonial .stripe{position:absolute;left:0;top:0;width:1200px;height:17px;background:#4a4e55}
.quote-mark{font:700 90px/1 Georgia,serif;color:#fff}
.quote-text{left:141px;top:125px;width:500px;font:18px/29px "Open Sans",sans-serif;color:#fff}
.quote-name{left:141px;top:250px;font:700 22px "Open Sans",sans-serif;color:var(--orange)}
.dots{left:532px;top:340px;display:flex;gap:16px}
.dots span{width:16px;height:16px;border-radius:50%;background:#fff}
.dots span:first-child{background:var(--orange)}
.partner{font:700 17px "Open Sans",sans-serif;color:#1d3b6b;top:163px}

/* contact */
.contact{left:0;top:2530px;width:1200px;height:384px;background:#fff}
.contact h2{position:absolute;top:44px;left:0;width:1200px;text-align:center;font:500 32px "Raleway",sans-serif;color:var(--blue)}
.field{height:48px;background:var(--field);color:#eee;font:600 15px "Open Sans",sans-serif;padding:14px 14px}
.contact .btn{left:491px;top:304px;width:205px;height:48px;font-size:15px;box-shadow:none}

/* footer */
.footer{left:0;top:2914px;width:1200px;height:275px;background:var(--dark);border-top:6px solid var(--orange)}
.footer h4{font:700 17px "Open Sans",sans-serif;color:#fff;letter-spacing:.5px}
.footer .col{top:84px;color:#cfd2d6}
.footer .links{left:95px;top:126px;font:600 13px/19px "Open Sans",sans-serif;color:#dfe2e6;letter-spacing:.6px}
.footer .about p{margin-top:16px;font:600 15px/24px "Open Sans",sans-serif;color:#8b9099;width:220px}
.footer .reach p{margin-top:14px;font:15px/24px "Open Sans",sans-serif;color:#dfe2e6}
.social{display:flex;gap:8px;margin-top:12px}
.social span{width:24px;height:24px;background:var(--orange)}
.newsletter .email{margin-top:20px;width:216px;height:35px;background:#fff;display:flex;align-items:center;gap:10px;padding-left:10px;font:14px "Open Sans",sans-serif;color:#999}
.newsletter .btn{margin-top:8px;width:216px;height:37px;font-size:14px;box-shadow:none}
.legal{left:0;top:3189px;width:1200px;height:54px;background:var(--darker);font:700 16px "Open Sans",sans-serif;color:#fff}
.legal .copy{left:95px;top:17px}
.legal .policy{left:880px;top:17px;color:var(--orange)}
.legal .policy b{color:#fff;font-weight:700}
</style>
</head>
<body>

<header>
  <div class="abs topbar">
    <div class="abs phone">
      <svg width="18" height="18" viewBox="0 0 18 18"><circle cx="9" cy="9" r="8" fill="none" stroke="#fff" stroke-width="1.4"/><path d="M6 5l1.6 1.8-.8 1.2c.6 1.2 1.5 2.1 2.7 2.7l1.2-.8L12.5 12l-1 1.2C8.2 12.6 5.4 9.8 4.8 6.5z" fill="#fff"/></svg>
      <span>(012) 555 0148</span>
    </div>
    <div class="abs account"><span>LOGIN</span><span>REGISTER</span></div>
    <svg class="abs search" width="20" height="20" viewBox="0 0 20 20"><circle cx="8" cy="8" r="6" fill="none" stroke="#fff" stroke-width="2.2"/><path d="M12.5 12.5l6 6" stroke="#fff" stroke-width="2.6" stroke-linecap="round"/></svg>
  </div>
  <nav class="abs mainnav">
    <a style="left:182px">HOME</a>
    <a style="left:296px">SERVICES</a>
    <a style="left:822px">BROKERS</a>
    <a style="left:956px">CONTACT US</a>
  </nav>
  <div class="abs brand-disc" style="top:-130px"><span class="brand-name">LarkfieldHR</span></div>
</header>

<section class="abs hero">
  <div role="img" aria-label="Two hands holding a paper cut-out strip of people, currency, puzzle pieces and a rising arrow against a blue background" style="position:absolute;inset:0"></div>
  <h1>GET YOUR FREE HR ASSESSMENT</h1>
  <a class="abs cta">TAKE ASSESSMENT</a>
  <div class="abs slider-arrow" style="left:0"><svg width="16" height="26" viewBox="0 0 16 26"><path d="M13 2L3 13l10 11" fill="none" stroke="#333" stroke-width="4"/></svg></div>
  <div class="abs slider-arrow" style="left:1161px"><svg width="16" height="26" viewBox="0 0 16 26"><path d="M3 2l10 11L3 24" fill="none" stroke="#333" stroke-width="4"/></svg></div>
</section>

<section class="abs services">
  <p class="abs intro">Gain a competitive advantage with the most trusted<br>and most used HR solutions and services.</p>

  <article class="abs card" style="left:82px">
    <svg width="64" height="64" viewBox="0 0 64 64"><circle cx="32" cy="32" r="20" fill="none" stroke="#0255a3" stroke-width="2" stroke-dasharray="4 3"/><circle cx="32" cy="28" r="6" fill="#0255a3"/><path d="M22 44c2-7 18-7 20 0z" fill="#0255a3"/><circle cx="10" cy="20" r="4" fill="#0255a3"/><circle cx="54" cy="20" r="4" fill="#0255a3"/><circle cx="10" cy="46" r="4" fill="#0255a3"/><circle cx="54" cy="46" r="4" fill="#0255a3"/></svg>
    <h3>HR Outsourcing</h3>
    <ul><li>Industry specialization</li><li>Decades of domain expertise</li><li>Employee onboarding</li><li>Benefits enrollment</li></ul>
    <a class="btn">LOAD MORE</a>
  </article>

  <article class="abs card" style="left:292px">
    <svg width="64" height="64" viewBox="0 0 64 64"><path d="M30 8l18 6v16c0 13-8 21-18 26-10-5-18-13-18-26V14z" fill="#0255a3"/><circle cx="44" cy="46" r="10" fill="#fff"/><circle cx="44" cy="46" r="8" fill="#0255a3"/><path d="M40 46l3 3 5-6" fill="none" stroke="#fff" stroke-width="2.4"/></svg>
    <h3>Safety</h3>
    <ul><li>Tax remitting and filing</li><li>Real-time entry</li><li>Payroll preview</li><li>Direct deposit</li></ul>
    <a class="btn">LOAD MORE</a>
  </article>

  <article class="abs card" style="left:504px">
    <svg width="64" height="64" viewBox="0 0 64 64"><circle cx="32" cy="32" r="26" fill="#0255a3"/><circle cx="32" cy="32" r="20" fill="#fff"/><path d="M32 18v15l9 6" fill="none" stroke="#0255a3" stroke-width="4" stroke-linecap="round"/></svg>
    <h3>Payroll / Timekeeping</h3>
    <ul><li>Health care insurance</li><li>Retirement plans</li><li>Flexible spending accounts</li><li>COBRA</li></ul>
    <a class="btn">LOAD MORE</a>
  </article>

  <article class="abs card" style="left:714px">
    <svg width="64" height="64" viewBox="0 0 64 64"><rect x="8" y="36" width="48" height="20" rx="2" fill="#0255a3"/><rect x="14" y="24" width="18" height="12" fill="#0255a3"/><rect x="34" y="18" width="16" height="18" fill="#0255a3"/><circle cx="23" cy="14" r="6" fill="#0255a3"/></svg>
    <h3>Benefits<br>Administration</h3>
    <ul><li>Employment Practices Liability Insurance (EPLI)</li><li>Unemployment</li><li>Affordable Care Act (ACA) support</li></ul>
    <a class="btn">LOAD MORE</a>
  </article>

  <article class="abs card" style="left:925px">
    <svg width="64" height="64" viewBox="0 0 64 64"><circle cx="32" cy="16" r="10" fill="#0255a3"/><path d="M14 58c0-18 8-28 18-28s18 10 18 28z" fill="#0255a3"/><path d="M29 32l3 4 3-4-2 20h-2z" fill="#fff"/></svg>
    <h3>Workers'<br>Compensation</h3>
    <ul><li>Mobile app</li><li>Robust reporting</li><li>Time off tracking</li><li>Expense reimbursement</li></ul>
    <a class="btn">LOAD MORE</a>
  </article>
</section>

<section class="abs stats">
  <div role="img" aria-label="Dim city skyline seen from above" style="position:absolute;inset:0"></div>
  <h2>We’re passionate about our partners’ success and empowering HR professionals.</h2>
  <div class="abs stat" style="left:54px">
    <svg width="48" height="48" viewBox="0 0 48 48"><path d="M14 6h20v12c0 7-4 12-10 12S14 25 14 18z" fill="#fff"/><path d="M14 10H6c0 7 4 10 8 10M34 10h8c0 7-4 10-8 10" fill="none" stroke="#fff" stroke-width="3"/><rect x="21" y="30" width="6" height="8" fill="#fff"/><rect x="14" y="38" width="20" height="5" fill="#fff"/></svg>
    <div class="num">7/10</div>
    <div class="label">7 of the top 10 brokers on<br>the Broker Ledger 100<br>list partner with Brisvane</div>
  </div>
  <div class="abs stat" style="left:244px">
    <svg width="56" height="48" viewBox="0 0 56 48"><path d="M2 16l12-6 10 4 8-4 10 2 12 6-6 14-14 8-10-6-14-4z" fill="#fff"/><path d="M22 20l8 6M26 28l6 4" stroke="#2d3139" stroke-width="2"/></svg>
    <div class="num">650</div>
    <div class="label">Insurance brokers and<br>and payroll bureaus<br>partner with Brisvane</div>
  </div>
  <div class="abs stat" style="left:435px">
    <svg width="60" height="48" viewBox="0 0 60 48"><circle cx="16" cy="16" r="7" fill="#fff"/><circle cx="44" cy="16" r="7" fill="#fff"/><circle cx="30" cy="14" r="9" fill="#fff"/><path d="M4 42c0-10 6-16 12-16s12 6 12 16zM32 42c0-10 6-16 12-16s12 6 12 16z" fill="#fff"/><path d="M16 44c0-12 6-20 14-20s14 8 14 20z" fill="#fff" stroke="#2d3139" stroke-width="2"/></svg>
    <div class="num">94,000</div>
    <div class="label">Employers nationwide</div>
  </div>
  <div class="abs stat" style="left:625px">
    <svg width="48" height="48" viewBox="0 0 48 48"><circle cx="24" cy="12" r="9" fill="#fff"/><path d="M6 46c0-16 8-24 18-24s18 8 18 24z" fill="#fff"/><path d="M24 24l-3 6 3 12 3-12z" fill="#2d3139"/></svg>
    <div class="num">13,000+</div>
    <div class="label">SMB customers</div>
  </div>
  <div class="abs stat" style="left:789px">
    <svg width="48" height="48" viewBox="0 0 48 48"><circle cx="22" cy="26" r="18" fill="none" stroke="#fff" stroke-width="4"/><circle cx="22" cy="26" r="10" fill="none" stroke="#fff" stroke-width="4"/><circle cx="22" cy="26" r="3" fill="#fff"/><path d="M22 26L42 6M36 4h6v6" fill="none" stroke="#fff" stroke-width="3"/></svg>
    <div class="num">25</div>
    <div class="label">Years in business</div>
  </div>
  <div class="abs stat" style="left:964px">
    <svg width="48" height="48" viewBox="0 0 48 48"><rect x="8" y="30" width="7" height="12" fill="#fff"/><rect x="19" y="22" width="7" height="20" fill="#fff"/><rect x="30" y="14" width="7" height="28" fill="#fff"/><path d="M8 22L34 4M28 3h7v7" fill="none" stroke="#fff" stroke-width="3"/><rect x="4" y="42" width="40" height="3" fill="#fff"/></svg>
    <div class="num">$31 Billion+</div>
    <div class="label">Payroll managed annually</div>
  </div>
</section>

<section class="abs blog">
  <h2>Recent Blog Posts</h2>
  <article class="abs post" style="left:78px">
    <h3>PELLENTESQUE HABITANT</h3>
    <p>Your budget is configured for optimum learning outcomes.</p>
    <div class="photo" role="img" aria-label="Colleagues smiling around a meeting table, background softly blurred"></div>
    <a class="more">READ MORE</a>
  </article>
  <article class="abs post" style="left:437px">
    <h3>PELLENTESQUE HABITANT</h3>
    <p>Your budget is configured for optimum learning outcomes.</p>
    <div class="photo" role="img" aria-label="Team discussion at a laptop in a bright office"></div>
    <a class="more">READ MORE</a>
  </article>
  <article class="abs post" style="left:798px">
    <h3>PELLENTESQUE HABITANT</h3>
    <p>Your budget is configured for optimum learning outcomes.</p>
    <div class="photo" role="img" aria-label="Business people reviewing documents across a desk"></div>
    <a class="more">READ MORE</a>
  </article>
  <a class="abs btn">LOAD MORE</a>
</section>

<section class="abs testimonial">
  <div class="backdrop" role="img" aria-label="Desaturated view of paperwork and a keyboard on a desk"></div>
  <div class="stripe"></div>
  <svg class="abs" style="left:0;top:0" width="1200" height="379" viewBox="0 0 1200 379">
    <polygon points="843,17 1200,17 1200,379 778,379 703,187" fill="#f37122"/>
    <polygon points="703,187 760,136 1200,136 1200,238 760,238" fill="#fff"/>
  </svg>
  <div class="abs quote-mark" style="left:80px;top:40px">“</div>
  <div class="abs quote-mark" style="left:636px;top:215px">”</div>
  <p class="abs quote-text">I love calling Larkfield HR because I know I’m going to get a direct answer about HR issues and not a lot of legal garble. They just ‘get to it’- so I can get back to business.</p>
  <p class="abs quote-name">Dana Whitfield, Director of HR</p>
  <span class="abs partner" style="left:712px">Northwell Mutual</span>
  <span class="abs partner" style="left:872px">Corvane Group</span>
  <span class="abs partner" style="left:1036px">Pellaris</span>
  <div class="abs dots"><span></span><span></span><span></span><span></span></div>
</section>

<section class="abs contact">
  <h2>Talk to a Team Member Today</h2>
  <div class="abs field" style="left:264px;top:114px;width:330px">First Name</div>
  <div class="abs field" style="left:605px;top:114px;width:325px">Last Name</div>
  <div class="abs field" style="left:264px;top:175px;width:330px">Company</div>
  <div class="abs field" style="left:605px;top:175px;width:325px">Phone</div>
  <div class="abs field" style="left:264px;top:237px;width:666px">Email</div>
  <a class="abs btn">SEND YOUR MESSAGE</a>
</section>

<footer class="abs footer">
  <div class="abs" style="left:95px;top:80px;font:700 24px 'Raleway',sans-serif;color:#fff">LarkfieldHR</div>
  <div class="abs links">HOME<br>SERVICES<br>BROKERS<br>CONTACT US</div>
  <div class="abs col about" style="left:346px">
    <h4>ABOUT BUSINESS</h4>
    <p>Lorem ipsum dolor sit amet, consec-tetur adipisicing elit, sed do elusmod tempor et incididunt ut labore et dolore</p>
  </div>
  <div class="abs col reach" style="left:640px">
    <h4>CONTACT US</h4>
    <p>info@larkfield-hr.example<br>(012) 555 0148</p>
    <div class="social"><span></span><span></span><span></span><span></span><span></span></div>
  </div>
  <div class="abs col newsletter" style="left:891px">
    <h4>SIGN UP NEWSLETTER</h4>
    <div class="email"><svg width="18" height="13" viewBox="0 0 18 13"><rect x="1" y="1" width="16" height="11" fill="none" stroke="#999" stroke-width="1.5"/><path d="M1 1l8 6 8-6" fill="none" stroke="#999" stroke-width="1.5"/></svg>Email Adress</div>
    <a class="btn">SUBSCRIBE</a>
  </div>
</footer>

<div class="abs legal">
  <span class="abs copy">2016 Harlow Crest, Inc. All rights reserved</span>
  <span class="abs policy">PRIVACY POLICY <b>&amp;</b> TERMS OF USE</span>
</div>

</body>
</html>
```